Improve the UI for two Mobile Apps

Brevano licenses ERP software to mid-sized companies (50M plus). Brevano's product suite includes procurement, accounting and CRM applications.

We have two mobile Apps that integrate with our ERP applications - Tallyway Hub and Morrow Field Kit. The Tallyway Hub App allows a user to review and approve requisitions, purchase orders, supplier invoices and expense reports which are forwarded to the App from our ERP applications. The expense report App allows a user to enter travel expenses and attach photos of receipts.

We are satisfied with the functionality of both mobile Apps. Our goal is to improve the aesthetics (fonts, colors, graphics). We are looking for a clean, light weight, modern design. The design should also be consistent with our current Brevano colors (blue and green) and branding (see www.brevanosystems.com).

Documentation showing current screen shots for each App is attached (2 files).
Updates

Please focus on the 14 major forms in the attachment. The larger document includes about 40 forms. It is intended to illustrate the use of the Apps which hopefully is useful when considering design alternatives. We realize the budget may be insufficient for the complete redesign of both Apps. When accepting the final design we will negotiate a price for revising / completing all forms. At this point we will increase the project's budget or complete the remaining work in-house. Thanks, Derek...

Target Market(s)

We sell to mid-large sized corporations. Are primary customer is the purchasing agent.

Industry/Entity Type

Accounting

Number of Pages Required

5+ page

Requirements
Must have
• Clean, modern design of the major entry forms shown in the attached documents. I need graphics and colors only. Our developers will adjust the Apps. I have attached 2 sets of documents. The first 2 files illustrate the use of all forms in both apps. Several forms appear multiple times. The second set of 3 files include the unique forms in both apps (14 in total). These files are labeled "(major forms)".

```html
<!DOCTYPE html>
<html lang="en">
<head>
<meta charset="utf-8">
<title>Edit Trip Info</title>
<link href="https://fonts.googleapis.com/css2?family=Roboto:ital,wght@0,400;0,500;0,700;1,400&display=swap" rel="stylesheet">
<style>
  :root {
    --status-bg: #0b1220;
    --status-fg: #ffffff;
    --status-dim: #6b7688;
    --header-bg: #ffffff;
    --header-line: #dde5ee;
    --title-blue: #1a3f8f;
    --brand-green: #3fae2a;
    --brand-green-dark: #2e8f1c;
    --body-top: #4f92c4;
    --body-bottom: #2a6896;
    --panel-bg: #2f6fb3;
    --panel-bg-light: #3b7fc2;
    --tab-active: #163f8c;
    --tab-idle: #a8c4da;
    --field-bg: #ffffff;
    --field-border: #c9d6e3;
    --text-dark: #1c2430;
    --footer-bg: #b7c4ce;
    --footer-line: #d7e0e7;
  }
  * { box-sizing: border-box; margin: 0; padding: 0; }
  html, body { width: 800px; height: 1200px; overflow: hidden; }
  body { font-family: "Roboto", Arial, sans-serif; background: var(--body-bottom); position: relative; }

  .status-bar {
    position: absolute; left: 0; top: 0; width: 800px; height: 60px;
    background: var(--status-bg); color: var(--status-fg);
    display: flex; align-items: center; justify-content: space-between; padding: 0 16px 0 18px;
  }
  .status-brand { font-size: 22px; font-weight: 700; }
  .status-right { display: flex; align-items: center; gap: 12px; }
  .status-time { font-size: 30px; font-weight: 400; }

  .app-header {
    position: absolute; left: 0; top: 60px; width: 800px; height: 150px;
    background: var(--header-bg);
    border-bottom: 1px solid var(--header-line);
    box-shadow: 0 3px 10px rgba(10, 30, 60, 0.18);
    z-index: 2;
  }
  .screen-title {
    position: absolute; left: 0; right: 0; top: 0; height: 150px;
    display: flex; align-items: center; justify-content: center;
    font-size: 40px; font-weight: 700; color: var(--title-blue); letter-spacing: 0.5px;
  }
  .save-button { position: absolute; left: 670px; top: 47px; }

  .screen-body {
    position: absolute; left: 0; top: 210px; width: 800px; height: 902px;
    background: linear-gradient(180deg, var(--body-top) 0%, var(--body-bottom) 100%);
  }

  .tab-row { position: absolute; left: 57px; top: 267px; height: 83px; display: flex; gap: 0; }
  .tab {
    height: 83px; border-radius: 12px 12px 0 0;
    display: flex; align-items: center; justify-content: center;
    font-size: 36px; color: #ffffff;
  }
  .tab-active { width: 285px; background: var(--tab-active); font-weight: 500; }
  .tab-idle { width: 285px; background: var(--tab-idle); font-weight: 400; }

  .tab-panel {
    position: absolute; left: 57px; top: 350px; width: 686px; height: 600px;
    background: linear-gradient(180deg, var(--panel-bg-light), var(--panel-bg));
    border-radius: 0 14px 14px 14px;
    box-shadow: 0 10px 24px rgba(8, 30, 60, 0.28);
  }
  .reason-field {
    position: absolute; left: 43px; top: 50px; width: 605px; height: 405px;
    background: var(--field-bg); border: 1px solid var(--field-border); border-radius: 8px;
    padding: 32px 26px; font-size: 28px; line-height: 44px; color: var(--text-dark);
    text-align: justify;
  }

  .app-footer {
    position: absolute; left: 0; top: 1112px; width: 800px; height: 88px;
    background: var(--footer-bg);
    border-top: 1px solid var(--footer-line);
  }
  .screen-code {
    position: absolute; right: 40px; top: 0; height: 88px;
    display: flex; align-items: center; font-size: 28px; color: #ffffff;
  }
</style>
</head>
<body>
  <div class="status-bar">
    <span class="status-brand">Brevano</span>
    <div class="status-right">
      <svg width="34" height="40" viewBox="0 0 34 40" aria-label="Signal">
        <text x="0" y="11" font-family="Roboto, sans-serif" font-size="11" fill="#ffffff">3G</text>
        <rect x="2" y="30" width="5" height="8" fill="#ffffff"/>
        <rect x="10" y="24" width="5" height="14" fill="#ffffff"/>
        <rect x="18" y="18" width="5" height="20" fill="#ffffff"/>
        <rect x="26" y="12" width="5" height="26" fill="var(--status-dim)"/>
      </svg>
      <svg width="20" height="38" viewBox="0 0 20 38" aria-label="Battery">
        <rect x="6" y="0" width="8" height="4" fill="var(--status-dim)"/>
        <rect x="1" y="4" width="18" height="33" rx="2" fill="none" stroke="var(--status-dim)" stroke-width="2"/>
        <rect x="4" y="20" width="12" height="14" fill="var(--status-dim)"/>
      </svg>
      <span class="status-time">11:38</span>
    </div>
  </div>

  <header class="app-header">
    <h1 class="screen-title">EDIT TRIP INFO</h1>
    <svg class="save-button" width="56" height="56" viewBox="0 0 56 56" aria-label="Save">
      <circle cx="28" cy="28" r="27" fill="var(--brand-green)"/>
      <path d="M16 29 L24.5 37.5 L40.5 20" fill="none" stroke="#ffffff" stroke-width="6.5" stroke-linecap="round" stroke-linejoin="round"/>
    </svg>
  </header>

  <main class="screen-body"></main>

  <nav class="tab-row">
    <div class="tab tab-active">Description</div>
    <div class="tab tab-idle">Accounting</div>
  </nav>
  <section class="tab-panel">
    <div class="reason-field">Please enter the reason for your trip or expenditure. Without it, you will not be able to Submit your report.</div>
  </section>

  <footer class="app-footer">
    <span class="screen-code">C6</span>
  </footer>
</body>
</html>
```